New business needs it's first website designed and coded for Wordpress

This is a new website for a new business. The business is called The Remote Tech Expert (TRTE). The business is based across multiple countries with the goal of providing workers in the Philippines opportunities to find work in international companies based in Australia, Singapore and New Zealand. The target market for TRTE is large enterprises (initially in Australia) looking for well legally structured business that knows how to recruit the top IT professionals and ensure that they are happy, all compliance, taxes and legals and professionally done and all services contracts are local to ensure enforceability.

We are looking for 10 pages (6 templates) for the website as follows:
Home
About Us
Services
Work from home full-timers
Work from office full-times
Work from home contractors
Work from office contractors
Careers Job Search
Employers Contact Us
Candidates Register your interest

Target Market(s)

IT Professionals in the Philippines & large enterprises in Australia, Singapore and New Zealand

Industry/Entity Type

IT Recruitment

Coding

Coded - Design and coding required

Number of Pages Required

5+ page

Requirements
Must have
• Please based style off logo file attached.

```html
<!DOCTYPE html>
<html lang="en">
<head>
<meta charset="utf-8">
<title>The Remote Tech Expert — Home</title>
<link href="https://fonts.googleapis.com/css2?family=Poppins:wght@400;500;600;700;800;900&family=Arimo:wght@400;700&family=Oswald:wght@300;400&display=swap" rel="stylesheet">
<style>
:root{
  --blue:#17a2e8;
  --blue-dark:#0f7fc0;
  --sky:#d8f0ff;
  --sky-2:#cdeeff;
  --panel:#e8f6ff;
  --navy:#1d2a44;
  --ink:#1b1b1b;
  --muted:#555d66;
  --grey-bg:#efefef;
  --footer:#0b0b0b;
  --white:#fff;
}
*{box-sizing:border-box;margin:0;padding:0}
html,body{width:1200px;height:4367px;overflow:hidden}
body{position:relative;background:var(--white);font-family:"Arimo",Arial,sans-serif;color:var(--ink)}
.abs{position:absolute}
.heading{font-family:"Poppins",sans-serif;font-weight:700;color:var(--navy);text-align:center;width:1200px;left:0;font-size:28px;letter-spacing:.3px}
.btn{position:absolute;display:flex;align-items:center;justify-content:center;gap:8px;font-family:"Poppins",sans-serif;font-weight:600;font-size:11px;color:#fff;background:var(--blue);border-radius:20px;text-transform:uppercase}
.btn svg{width:14px;height:10px}
.rule{position:absolute;left:112px;width:975px;height:1px;background:#9fb4c6}
.circle-arrow{width:20px;height:20px;border-radius:50%;background:var(--blue);display:flex;align-items:center;justify-content:center}

/* header */
.site-header{position:absolute;left:0;top:0;width:1200px;height:63px;background:#fff}
.brand{position:absolute;left:112px;top:14px;display:flex;align-items:center;gap:8px;font-family:"Poppins",sans-serif;font-weight:800;font-size:30px;color:var(--navy)}
.brand .mark{width:16px;height:16px;background:var(--blue)}
.nav{position:absolute;top:25px;font-family:"Poppins",sans-serif;font-size:11px;font-weight:500;color:var(--navy)}
.nav.active{color:var(--blue)}

/* hero */
.hero{position:absolute;left:0;top:63px;width:1200px;height:459px;background:var(--sky);overflow:hidden}
.hero .blob{position:absolute;border-radius:50%;background:#bfe4fb}
.hero-art{position:absolute;left:700px;top:10px;width:440px;height:449px;border-radius:40% 40% 0 0;background:linear-gradient(160deg,#bfe3fa,#7cc6ef 60%,#4aa9e0)}
.hero-kicker{position:absolute;left:112px;top:172px;font-family:"Poppins",sans-serif;font-weight:800;font-size:36px;color:var(--navy);transform:rotate(-4deg);transform-origin:left}
.hero-title{position:absolute;left:104px;top:195px;font-family:"Poppins",sans-serif;font-weight:900;font-size:112px;letter-spacing:-2px;color:var(--blue);transform:rotate(-3deg);transform-origin:left;line-height:1.1}
.hero-sub{position:absolute;left:236px;top:320px;font-family:"Oswald",sans-serif;font-weight:300;font-size:40px;letter-spacing:14px;color:var(--blue)}

.search{position:absolute;left:370px;top:492px;width:458px;height:60px;background:#fff;border-radius:6px;box-shadow:0 4px 16px rgba(30,80,120,.15)}
.field{position:absolute;top:12px;height:36px;width:142px;border:1px solid #c7d3dc;border-radius:6px;display:flex;align-items:center;gap:14px;padding-left:10px;font-size:11px;color:#222}
.search .btn{top:12px;left:327px;width:116px;height:36px}

/* services */
.service{position:absolute;top:658px;width:232px;height:291px;border-radius:6px;overflow:hidden;background:linear-gradient(180deg,#b9b6b2 0%,#8d8984 55%,#3b3a39 100%)}
.service .label{position:absolute;left:18px;bottom:20px;font-family:"Poppins",sans-serif;font-weight:500;font-size:14px;line-height:1.35;color:#fff}
.service .circle-arrow{position:absolute;right:12px;bottom:22px}

/* jobs */
.job{position:absolute;width:312px;height:272px;background:linear-gradient(180deg,#fff,#f4faff);border:1px solid #e3edf3;border-radius:6px}
.job .logo{position:absolute;left:18px;top:20px;width:34px;height:34px;border-radius:50%;background:var(--navy)}
.job .company{position:absolute;left:64px;top:33px;font-size:10px;color:#333}
.job .posted{position:absolute;right:16px;top:33px;font-size:10px;color:#333;display:flex;gap:6px;align-items:center}
.job .posted i{width:9px;height:7px;background:var(--blue);display:block}
.job .title{position:absolute;left:18px;top:66px;font-family:"Poppins",sans-serif;font-weight:500;font-size:17px;color:#111}
.job .tags{position:absolute;left:18px;top:102px;display:flex;gap:6px}
.tag{font-size:9px;background:#e2f1fb;color:#223;padding:4px 8px;border-radius:3px}
.tag.loc{background:#bfe2f7}
.job .desc{position:absolute;left:20px;top:134px;width:270px;font-size:10.5px;line-height:18px;color:#333}
.job .apply{position:absolute;left:20px;top:210px;width:112px;height:32px;border-radius:16px;background:#3f4247;color:#fff;font-family:"Poppins",sans-serif;font-weight:600;font-size:9.5px;display:flex;align-items:center;justify-content:center;gap:8px}

/* testimonial */
.testimonial{position:absolute;left:112px;top:1792px;width:975px;height:268px;background:var(--sky-2);border-radius:6px;text-align:center}
.quote-mark{position:absolute;left:425px;top:-10px;font-family:"Poppins",sans-serif;font-weight:900;font-size:190px;line-height:1;color:#9fd6f5}
.avatar{position:absolute;left:448px;top:50px;width:66px;height:66px;border-radius:50%;background:linear-gradient(#6c7682,#3a4350);border:4px solid #fff;box-shadow:0 0 0 3px var(--blue)}
.testimonial p{position:absolute;left:0;top:135px;width:975px;font-size:14px;line-height:21px;color:#333}
.testimonial .who{position:absolute;left:0;top:193px;width:975px;font-size:14px;font-weight:700;color:#222}
.stars{position:absolute;left:437px;top:220px;display:flex;gap:2px}
.slide{position:absolute;top:130px;width:30px;height:30px;border-radius:50%;background:var(--blue);display:flex;align-items:center;justify-content:center}

/* about */
.about{position:absolute;left:0;top:2107px;width:1200px;height:693px;background:var(--grey-bg);overflow:hidden}
.about .heading{top:36px}
.about p{position:absolute;left:240px;top:80px;width:720px;text-align:center;font-size:11px;line-height:19px;color:#333}
.about-photo{position:absolute;left:0;top:230px;width:1200px;height:463px;background:linear-gradient(180deg,#e9e8e7 0%,#d6d2cf 40%,#a9b4c0 70%,#8a8480 100%)}

/* destinations */
.dest{position:absolute;top:2950px;width:360px;height:440px}
.dest .ring{position:absolute;left:63px;top:0;width:230px;height:230px;border-radius:50%;border:2px solid var(--navy)}
.dest .icon{position:absolute;left:118px;top:70px;width:120px;height:110px;border-radius:12px;background:linear-gradient(#a9dbf7,#5bb4e6)}
.dest .panel{position:absolute;left:88px;top:218px;width:210px;height:222px;background:var(--panel)}
.dest .name{position:absolute;left:98px;top:214px;width:164px;height:40px;background:var(--navy);color:#fff;font-family:"Poppins",sans-serif;font-weight:500;font-size:17px;display:flex;align-items:center;justify-content:center}
.dest ul{position:absolute;left:110px;top:270px;list-style:none}
.dest li{position:relative;padding-left:22px;margin-bottom:20px;font-size:13px;line-height:18px;color:#333}
.dest li b{color:var(--navy);font-size:13.5px}
.dest li::before{content:"";position:absolute;left:0;top:6px;width:6px;height:6px;border-radius:50%;background:var(--navy)}

/* blog */
.post{position:absolute;top:3495px;width:312px;height:251px;overflow:hidden;background:#fff}
.post .img{position:absolute;left:0;top:0;width:312px;height:210px}
.post .date{position:absolute;left:14px;top:0;width:34px;padding-top:4px;background:#fff;text-align:center;font-size:9px;line-height:11px;color:#222}
.post .date span{display:block;background:var(--blue);color:#fff;font-weight:700;margin-top:2px;padding:1px 0}
.post .caption{position:absolute;left:8px;top:180px;width:296px;height:71px;background:#fff;padding:16px 12px;font-family:"Poppins",sans-serif;font-weight:500;font-size:13.5px;line-height:19px;color:#222}
.post .circle-arrow{position:absolute;right:18px;top:218px}

/* cta */
.cta{position:absolute;left:0;top:3868px;width:1200px;height:234px;background:var(--blue);overflow:hidden}
.cta .ghost{position:absolute;left:730px;top:80px;font-family:"Poppins",sans-serif;font-weight:900;font-size:180px;line-height:1;color:rgba(255,255,255,.14)}
.cta h2{position:absolute;left:0;top:52px;width:1200px;text-align:center;font-family:"Poppins",sans-serif;font-weight:700;font-size:30px;color:#fff}
.cta p{position:absolute;left:0;top:96px;width:1200px;text-align:center;font-size:11px;color:#fff}
.cta .contact{position:absolute;left:533px;top:130px;width:132px;height:38px;border-radius:20px;background:#fff;color:var(--blue);font-family:"Poppins",sans-serif;font-weight:600;font-size:11px;display:flex;align-items:center;justify-content:center;gap:8px}
.cta-person{position:absolute;left:100px;top:3805px;width:260px;height:297px;border-radius:120px 120px 0 0;background:linear-gradient(180deg,#c9b39a,#4f7fb0 55%,#3c6c9c)}

/* footer */
.site-footer{position:absolute;left:0;top:4102px;width:1200px;height:265px;background:var(--footer);color:#fff}
.site-footer .brand{left:112px;top:30px;color:#fff;font-size:26px}
.site-footer .brand .mark{background:#fff}
.f-about{position:absolute;left:112px;top:84px;width:180px;font-size:8.5px;line-height:14px;color:#ddd}
.f-sep{position:absolute;top:30px;width:1px;height:180px;background:#333}
.f-col{position:absolute;top:46px}
.f-col h4{font-family:"Poppins",sans-serif;font-weight:700;font-size:12px;margin-bottom:14px}
.f-col a{display:flex;align-items:center;gap:10px;font-size:8.5px;color:#ddd;text-decoration:none;margin-bottom:10px;height:14px}
.f-dot{width:14px;height:14px;border-radius:50%;background:var(--blue);flex:none}
.f-email{width:182px;height:30px;background:#2a2a2a;border-radius:3px;font-size:8.5px;color:#ddd;padding:10px 14px}
.f-sub{margin-top:14px;width:132px;height:36px;border-radius:20px;background:var(--blue);font-family:"Poppins",sans-serif;font-weight:700;font-size:10px;display:flex;align-items:center;justify-content:center;gap:14px}
.copyright{position:absolute;left:0;top:238px;width:1200px;text-align:center;font-size:8px;color:#ccc}
</style>
</head>
<body>

<svg width="0" height="0" style="position:absolute">
  <defs>
    <symbol id="arrow" viewBox="0 0 14 10"><path d="M0 5h12M8 1l4 4-4 4" fill="none" stroke="currentColor" stroke-width="1.5"/></symbol>
    <symbol id="star" viewBox="0 0 20 20"><path d="M10 1l2.7 5.6 6.1.9-4.4 4.3 1 6.1L10 15l-5.4 2.9 1-6.1L1.2 7.5l6.1-.9z" fill="#f5b400"/></symbol>
  </defs>
</svg>

<!-- Header -->
<header class="site-header">
  <div class="brand"><span class="mark"></span>TRTE</div>
  <span class="nav active" style="left:414px">HOME</span>
  <span class="nav" style="left:474px">ABOUT US</span>
  <span class="nav" style="left:557px">SERVICES ⌄</span>
  <span class="nav" style="left:637px">CAREERS JOB SEARCH</span>
  <span class="nav" style="left:787px">EMPLOYERS CONTACT US</span>
  <div class="btn" style="left:960px;top:15px;width:126px;height:33px;font-size:10px">Register now <svg><use href="#arrow"/></svg></div>
</header>

<!-- Hero -->
<section class="hero">
  <div class="blob" style="left:-60px;top:300px;width:200px;height:200px"></div>
  <div class="blob" style="left:980px;top:-10px;width:120px;height:120px;opacity:.6"></div>
  <div class="blob" style="left:705px;top:360px;width:30px;height:30px"></div>
  <div class="blob" style="left:1120px;top:40px;width:150px;height:150px;opacity:.7"></div>
  <div class="hero-art" role="img" aria-label="Illustration of a hand holding a megaphone"></div>
  <div class="hero-kicker">EXPLORE YOUR DREAM JOB</div>
  <div class="hero-title">JOIN US</div>
  <div class="hero-sub">WE ARE HIRING</div>
</section>

<div class="search">
  <div class="field" style="left:11px">
    <svg width="11" height="11" viewBox="0 0 12 12"><circle cx="5" cy="5" r="4" fill="none" stroke="#222" stroke-width="1.5"/><path d="M8 8l3 3" stroke="#222" stroke-width="1.5"/></svg>Keywords</div>
  <div class="field" style="left:166px">
    <svg width="10" height="12" viewBox="0 0 10 14"><path d="M5 13S1 8 1 5a4 4 0 018 0c0 3-4 8-4 8z" fill="#222"/><circle cx="5" cy="5" r="1.5" fill="#fff"/></svg>Location</div>
  <div class="btn">Find job <svg><use href="#arrow"/></svg></div>
</div>

<!-- Services -->
<h2 class="heading abs" style="top:596px">OUR SERVICES</h2>
<div class="service" style="left:112px" role="img" aria-label="Photo of a man working on a laptop at home"><div class="label">Work from<br>Home full-timers</div><div class="circle-arrow"><svg width="10" height="8" style="color:#fff"><use href="#arrow"/></svg></div></div>
<div class="service" style="left:360px" role="img" aria-label="Photo of a woman working in an office"><div class="label">Work from<br>Office full-timers</div><div class="circle-arrow"><svg width="10" height="8" style="color:#fff"><use href="#arrow"/></svg></div></div>
<div class="service" style="left:607px" role="img" aria-label="Photo of a contractor working from a home kitchen"><div class="label">Work from<br>Home Contractors</div><div class="circle-arrow"><svg width="10" height="8" style="color:#fff"><use href="#arrow"/></svg></div></div>
<div class="service" style="left:855px" role="img" aria-label="Photo of two colleagues discussing work in an office"><div class="label">Work from<br>Office contractors</div><div class="circle-arrow"><svg width="10" height="8" style="color:#fff"><use href="#arrow"/></svg></div></div>

<div class="rule" style="top:1000px"></div>
<div class="btn" style="left:514px;top:981px;width:172px;height:38px">View all services <svg><use href="#arrow"/></svg></div>

<!-- Featured jobs -->
<h2 class="heading abs" style="top:1060px">FEATURED JOBS</h2>

<article class="job" style="left:112px;top:1115px"><span class="logo"></span><span class="company">Gridline Inc</span><span class="posted"><i></i>Posted on 1.11.24</span><h3 class="title">Product Designer</h3><div class="tags"><span class="tag loc">⚲ Berlyn</span><span class="tag">▪ Full Time</span><span class="tag">$ 80k-50k</span></div><p class="desc">Lorem ipsum dolor sit amet, consectetur adipiscing elit. Nulla vulputate est vel urna tincidunt, eu mollis metus lobortis.</p><div class="apply">APPLY NOW <svg width="12" height="8" style="color:#fff"><use href="#arrow"/></svg></div></article>
<article class="job" style="left:443px;top:1115px"><span class="logo" style="background:#e8424a"></span><span class="company">Nestly</span><span class="posted"><i></i>Posted on 1.11.24</span><h3 class="title">UI/UX Designer</h3><div class="tags"><span class="tag loc">⚲ Berlyn</span><span class="tag">▪ Full Time</span><span class="tag">$ 80k-50k</span></div><p class="desc">Lorem ipsum dolor sit amet, consectetur adipiscing elit. Nulla vulputate est vel urna tincidunt, eu mollis metus lobortis.</p><div class="apply">APPLY NOW <svg width="12" height="8" style="color:#fff"><use href="#arrow"/></svg></div></article>
<article class="job" style="left:775px;top:1115px"><span class="logo" style="background:#7cb342"></span><span class="company">Cartwell</span><span class="posted"><i></i>Posted on 1.11.24</span><h3 class="title">iOS Developer</h3><div class="tags"><span class="tag loc">⚲ Berlyn</span><span class="tag">▪ Full Time</span><span class="tag">$ 80k-50k</span></div><p class="desc">Lorem ipsum dolor sit amet, consectetur adipiscing elit. Nulla vulputate est vel urna tincidunt, eu mollis metus lobortis.</p><div class="apply">APPLY NOW <svg width="12" height="8" style="color:#fff"><use href="#arrow"/></svg></div></article>

<article class="job" style="left:112px;top:1404px"><span class="logo" style="background:#111"></span><span class="company">Ridewise</span><span class="posted"><i></i>Posted on 1.11.24</span><h3 class="title">Creative Director</h3><div class="tags"><span class="tag loc">⚲ Berlyn</span><span class="tag">▪ Full Time</span><span class="tag">$ 80k-50k</span></div><p class="desc">Lorem ipsum dolor sit amet, consectetur adipiscing elit. Nulla vulputate est vel urna tincidunt, eu mollis metus lobortis.</p><div class="apply">APPLY NOW <svg width="12" height="8" style="color:#fff"><use href="#arrow"/></svg></div></article>
<article class="job" style="left:443px;top:1404px"><span class="logo" style="background:#1877f2"></span><span class="company">Chatterly</span><span class="posted"><i></i>Posted on 1.11.24</span><h3 class="title">Marketing Manager</h3><div class="tags"><span class="tag loc">⚲ Berlyn</span><span class="tag">▪ Full Time</span><span class="tag">$ 80k-50k</span></div><p class="desc">Lorem ipsum dolor sit amet, consectetur adipiscing elit. Nulla vulputate est vel urna tincidunt, eu mollis metus lobortis.</p><div class="apply">APPLY NOW <svg width="12" height="8" style="color:#fff"><use href="#arrow"/></svg></div></article>
<article class="job" style="left:775px;top:1404px"><span class="logo" style="background:#222"></span><span class="company">Optiva</span><span class="posted"><i></i>Posted on 1.11.24</span><h3 class="title">Software Engineer</h3><div class="tags"><span class="tag loc">⚲ Berlyn</span><span class="tag">▪ Full Time</span><span class="tag">$ 80k-50k</span></div><p class="desc">Lorem ipsum dolor sit amet, consectetur adipiscing elit. Nulla vulputate est vel urna tincidunt, eu mollis metus lobortis.</p><div class="apply">APPLY NOW <svg width="12" height="8" style="color:#fff"><use href="#arrow"/></svg></div></article>

<div class="rule" style="top:1727px"></div>
<div class="btn" style="left:528px;top:1708px;width:146px;height:38px">View all jobs <svg><use href="#arrow"/></svg></div>

<!-- Testimonial -->
<section class="testimonial">
  <div class="quote-mark">“</div>
  <div class="avatar" role="img" aria-label="Portrait of the reviewer"></div>
  <p>“Perfect platform for real jobs in the IT world. The job postings direct you<br>to a recruiter for the company or to the company's website itself.”</p>
  <div class="who">Marisol T., Tech Professional</div>
  <div class="stars"><svg width="18" height="18"><use href="#star"/></svg><svg width="18" height="18"><use href="#star"/></svg><svg width="18" height="18"><use href="#star"/></svg><svg width="18" height="18"><use href="#star"/></svg><svg width="18" height="18"><use href="#star"/></svg></div>
  <div class="slide" style="left:63px"><svg width="10" height="10" viewBox="0 0 10 10"><path d="M7 1L3 5l4 4" fill="none" stroke="#fff" stroke-width="2"/></svg></div>
  <div class="slide" style="left:879px"><svg width="10" height="10" viewBox="0 0 10 10"><path d="M3 1l4 4-4 4" fill="none" stroke="#fff" stroke-width="2"/></svg></div>
</section>

<!-- About -->
<section class="about">
  <h2 class="heading abs">ABOUT THE REMOTE TECH EXPERT</h2>
  <p>The business is based across multiple countries with the goal of providing workers in the Philippines opportunities to find work in international companies based in Australia, Singapore and New Zealand. The target market for TRTE is large enterprises (initially in Australia) looking for well legally structured business that knows how to recruit the top IT professionals and ensure that they are happy, all compliance, taxes and legals and professionally done and all services contracts are local to ensure enforceability.</p>
  <div class="btn" style="left:533px;top:175px;width:132px;height:36px">Read more <svg><use href="#arrow"/></svg></div>
  <div class="about-photo" role="img" aria-label="Photo of a diverse group of professionals seated in a row holding signs reading 150M+ Candidates, 30M+ Resumes, 10M+ Text Subscribers and 97% Customer satisfaction rating"></div>
</section>

<!-- Destinations -->
<h2 class="heading abs" style="top:2842px;line-height:40px;font-size:29px">DISCOVER THE THOUSAND OF<br>JOBS AROUND YOUR DESTINATION</h2>

<div class="dest" style="left:60px">
  <div class="ring"></div><div class="icon" role="img" aria-label="Line illustration of a New Zealand landmark building"></div>
  <div class="panel"></div><div class="name">New Zealand</div>
  <ul><li><b>San Francisco, CA</b><br>22,913 vacancies</li><li><b>Austin, TX</b><br>15,862 vacancies</li><li><b>Seattle, WA</b><br>12,185 vacancies</li></ul>
</div>
<div class="dest" style="left:420px">
  <div class="ring"></div><div class="icon" role="img" aria-label="Line illustration of a Singapore landmark"></div>
  <div class="panel"></div><div class="name">Singapore</div>
  <ul><li><b>Atlanta, GA</b><br>22,913 vacancies</li><li><b>Phoenix, AZ</b><br>15,862 vacancies</li><li><b>San Diego, CA</b><br>12,185 vacancies</li></ul>
</div>
<div class="dest" style="left:780px">
  <div class="ring"></div><div class="icon" role="img" aria-label="Line illustration of the Sydney Opera House"></div>
  <div class="panel"></div><div class="name">Australia</div>
  <ul><li><b>Boston, MA</b><br>22,913 vacancies</li><li><b>Philadelphia, PA</b><br>15,862 vacancies</li><li><b>Nashville, TN</b><br>12,185 vacancies</li></ul>
</div>

<!-- Blog -->
<h2 class="heading abs" style="top:3434px">LATEST BLOG</h2>
<article class="post" style="left:112px">
  <div class="img" role="img" aria-label="Photo of a hand holding a funnel over people icons" style="background:linear-gradient(135deg,#2c3440,#56606c 60%,#9aa2aa)"></div>
  <div class="date">Oct<br>31<span>2024</span></div>
  <div class="caption">Candidate Funnel: Optimize Your Hiring Process for Better Results.</div>
  <div class="circle-arrow"><svg width="10" height="8" style="color:#fff"><use href="#arrow"/></svg></div>
</article>
<article class="post" style="left:444px">
  <div class="img" role="img" aria-label="Photo of a recruiter reviewing a resume" style="background:linear-gradient(135deg,#e6e6e6,#bcbcbc 55%,#5d5550)"></div>
  <div class="date">Oct<br>31<span>2024</span></div>
  <div class="caption">How should recruiters use interview intelligence platform?</div>
  <div class="circle-arrow"><svg width="10" height="8" style="color:#fff"><use href="#arrow"/></svg></div>
</article>
<article class="post" style="left:775px">
  <div class="img" role="img" aria-label="Photo of people working with a tablet and documents" style="background:linear-gradient(135deg,#d7d7d7,#8a8a8a 60%,#4a4a4a)"></div>
  <div class="date">Oct<br>31<span>2024</span></div>
  <div class="caption">Benefits of Hiring Interim CEOs and Consultants</div>
  <div class="circle-arrow"><svg width="10" height="8" style="color:#fff"><use href="#arrow"/></svg></div>
</article>

<div class="btn" style="left:528px;top:3774px;width:144px;height:38px">View all blog <svg><use href="#arrow"/></svg></div>

<!-- CTA -->
<section class="cta">
  <div class="ghost">TRTE</div>
  <h2>READY TO WORK WITH US?</h2>
  <p>We're ready to work with you to help you reach your hiring goals.</p>
  <div class="contact">CONTACT US <svg width="12" height="8"><use href="#arrow"/></svg></div>
</section>
<div class="cta-person" role="img" aria-label="Photo of a smiling man pointing towards the call to action"></div>

<!-- Footer -->
<footer class="site-footer">
  <div class="brand"><span class="mark"></span>TRTE</div>
  <p class="f-about">The business is called The Remote Tech Expert (TRTE). The business is based across multiple countries with the goal of providing workers in the Philippines opportunities to find work in international companies based in Australia, Singapore and New Zealand.</p>
  <div class="f-sep" style="left:305px"></div>
  <div class="f-col" style="left:330px"><h4>CONTACT US</h4>
    <a><span class="f-dot"></span>Australia, Singapore and New Zealand</a>
    <a style="color:#6cc4f5"><span class="f-dot"></span>hello@remotetechexpert.example</a>
    <a><span class="f-dot"></span>555-210-0147</a></div>
  <div class="f-sep" style="left:538px"></div>
  <div class="f-col" style="left:562px"><h4>MAIN LINKS</h4>
    <a style="margin-bottom:4px">Home</a><a style="margin-bottom:4px">About Us</a><a style="margin-bottom:4px">Services</a><a style="margin-bottom:4px">Careers Job Search</a><a style="margin-bottom:4px">Employers Contact Us</a><a style="margin-bottom:4px">Candidates Register your interest</a></div>
  <div class="f-sep" style="left:728px"></div>
  <div class="f-col" style="left:750px"><h4>FOLLOW US</h4>
    <a><span class="f-dot"></span>Chatterly</a><a><span class="f-dot"></span>ProLinkr</a><a><span class="f-dot"></span>Chirpline</a></div>
  <div class="f-sep" style="left:888px"></div>
  <div class="f-col" style="left:905px"><h4>SUBSCRIBE NEWSLETTER</h4>
    <div class="f-email">Enter Your Email</div>
    <div class="f-sub">SUBSCRIBE <svg width="14" height="10"><use href="#arrow"/></svg></div></div>
  <div class="copyright">© The Remote Tech Expert 2024 All Rights Reserved</div>
</footer>

</body>
</html>
```